Design for Wet Paper Tape

Hi there,

I am looking for a Wet Paper Tape Design, 1 colour (black) for a vintage lighting manufacturer. Width is 70mm (+5mm bleed) and length is 381,0011mm. This tape is used to close a parcel.

We've made already two designs showing company name and brand name including logos with an 25° inclined writing. However, brand name (Dawnfold) and especially company name (Ferncastle) are difficult to read by the client.

So I am looking for an improvement of the existing design. Costumer should be able to identify brand and company name. It should underline the vintage character of our brand and products. The writing of the Ferncastle logo doesn't have to be 100 % accurate. Font can be slightly adapted for better readings. I prefer to use the whole width of the tape.

```html
<!DOCTYPE html>
<html lang="en">
<head>
<meta charset="utf-8">
<title>Dawnfold Parcel Tape</title>
<link rel="stylesheet" href="https://fonts.googleapis.com/css2?family=Lato:wght@400;700;900&display=swap">
<style>
  :root {
    --backdrop: #404040;
    --tape: #ffffff;
    --ink: #000000;
  }
  html, body {
    margin: 0;
    padding: 0;
    width: 1200px;
    height: 1200px;
    overflow: hidden;
    background: var(--backdrop);
  }
  .canvas {
    position: relative;
    width: 1200px;
    height: 1200px;
    background: var(--backdrop);
    font-family: "Lato", sans-serif;
  }
  .tape {
    position: absolute;
    left: 487px;
    top: 47px;
    width: 226px;
    height: 1092px;
    background: var(--tape);
    overflow: hidden;
    box-shadow: 4px 6px 10px rgba(0, 0, 0, 0.35);
  }
  .brand-tag {
    position: absolute;
    left: 26px;
    top: 48px;
    margin: 0;
    font-size: 20px;
    font-weight: 700;
    letter-spacing: 0.5px;
    color: var(--ink);
  }
  .slogan-line {
    position: absolute;
    margin: 0;
    font-size: 98px;
    font-weight: 700;
    line-height: 1;
    color: var(--ink);
    white-space: nowrap;
    transform-origin: 0 0;
    transform: rotate(70deg);
  }
  .slogan-line--first  { left: 205px; top: -115px; }
  .slogan-line--second { left: 118px; top: 95px; }
  .slogan-line--third  { left: 40px;  top: 255px; }
  .maker {
    position: absolute;
    left: 0;
    width: 100%;
    top: 868px;
    text-align: center;
  }
  .maker-name {
    margin: 0;
    font-size: 31px;
    font-weight: 700;
    color: var(--ink);
  }
  .maker-mark {
    display: block;
    width: 114px;
    height: 114px;
    margin: 28px auto 0;
    background: var(--ink);
  }
</style>
</head>
<body>
<main class="canvas">
  <section class="tape">
    <p class="brand-tag">Dawnfold</p>
    <p class="slogan-line slogan-line--first">Dawnfold</p>
    <p class="slogan-line slogan-line--second">Dawnfold</p>
    <p class="slogan-line slogan-line--third">Dawnfold</p>
    <div class="maker">
      <p class="maker-name">Ferncastle</p>
      <span class="maker-mark"></span>
    </div>
  </section>
</main>
</body>
</html>
```